Bed Company needs business card

Hello, we are a bed company that makes specialized magnets for beds. We are an alternative healing company. I need a modern and upscale business card. Please incorporate my logo for the card.

Accepted file formats are AI, EPS, and Press-Ready PDFS.

Please include all fonts or convert them to outlines regardless of file type.

If you are designing the card in Photoshop the file Must be 1200dpi.

I am open to anything for the business card.  I really like all of your designs and if you want to change the color of the logo, you can.  I will be making the final selection by Friday.  Thank You for all of your designs.  Feel Free to submit different color logos if you want.  

Reason: I will make a decision Final on Friday April 20th. 2012. Good Luck and Thank you all for the designs.

Target Market(s)

My target Market is people, who are looking for alternative healing.

Industry/Entity Type

Business

Requirements
Must have
• My logo must be incorporated. The front card must have

Name
Job Title

Address
Work
Cell
Fax
email
web

Just put in fake info for the card.

The back of the card. I want the logo on the back with color. I just want it to look modern and cool.

```html
<!DOCTYPE html>
<html lang="en">
<head>
<meta charset="utf-8">
<title>Lodestone Rest – Business Card</title>
<link href="https://fonts.googleapis.com/css2?family=Open+Sans:wght@400;700&display=swap" rel="stylesheet">
<style>
  :root {
    --backdrop: #1b1b1b;
    --card-white: #ffffff;
    --brand-green: #2a8a3e;
    --band-green: #156b38;
    --rule-green: #2f9a47;
    --band-text: #ffffff;
    --divider: rgba(255,255,255,0.55);
  }
  * { margin: 0; padding: 0; box-sizing: border-box; }
  html, body {
    width: 1200px; height: 1130px; overflow: hidden;
    background: var(--backdrop);
    font-family: "Open Sans", Arial, sans-serif;
  }
  .canvas { position: relative; width: 1200px; height: 1130px; }
  .card {
    position: absolute; width: 783px; height: 447px;
    background: var(--card-white); border-radius: 30px; overflow: hidden;
  }
  .card-front { left: 82px; top: 79px; }
  .card-back { left: 320px; top: 603px; }

  .brand { position: absolute; display: flex; align-items: center; gap: 18px; }
  .brand-mark { width: 64px; height: 64px; background: var(--brand-green); flex: none; }
  .brand-text { display: flex; flex-direction: column; align-items: flex-end; }
  .brand-name {
    font-weight: 700; color: var(--brand-green); line-height: 1; white-space: nowrap;
  }
  .brand-tagline {
    font-weight: 400; color: var(--brand-green); line-height: 1; margin-top: 8px; letter-spacing: 0.5px;
  }
  .card-front .brand { left: 122px; top: 146px; }
  .card-front .brand-name { font-size: 56px; }
  .card-front .brand-tagline { font-size: 24px; }

  .card-back .brand { left: 150px; top: 58px; }
  .card-back .brand-name { font-size: 52px; }
  .card-back .brand-tagline { font-size: 22px; }

  .rule { position: absolute; left: 0; top: 240px; width: 100%; height: 4px; background: var(--rule-green); }
  .band { position: absolute; left: 0; top: 250px; width: 100%; bottom: 0; background: var(--band-green); }

  .identity {
    position: absolute; right: 427px; top: 278px; text-align: right; color: var(--band-text);
  }
  .person-name { font-size: 23px; font-weight: 700; line-height: 1.2; }
  .person-title { font-size: 19px; line-height: 1.3; }
  .address { margin-top: 20px; font-size: 19px; line-height: 1.4; }

  .divider { position: absolute; left: 384px; top: 270px; width: 2px; height: 160px; background: var(--divider); }

  .contacts { position: absolute; left: 412px; top: 284px; list-style: none; color: var(--band-text); font-size: 19px; }
  .contacts li { display: flex; align-items: center; gap: 10px; height: 32px; }
  .contacts svg { width: 16px; height: 16px; flex: none; fill: var(--band-text); }
</style>
</head>
<body>
<div class="canvas">

  <section class="card card-front">
    <div class="brand">
      <span class="brand-mark"></span>
      <div class="brand-text">
        <span class="brand-name">Lodestone Rest</span>
        <span class="brand-tagline">Alternative Healing</span>
      </div>
    </div>
  </section>

  <section class="card card-back">
    <div class="brand">
      <span class="brand-mark"></span>
      <div class="brand-text">
        <span class="brand-name">Lodestone Rest</span>
        <span class="brand-tagline">Alternative Healing</span>
      </div>
    </div>

    <div class="rule"></div>
    <div class="band"></div>

    <div class="identity">
      <p class="person-name">Daniel Morrow</p>
      <p class="person-title">Vice-President</p>
      <p class="address">214 Orchard Lane<br>Glendale, CA 91204</p>
    </div>

    <div class="divider"></div>

    <ul class="contacts">
      <li>
        <svg viewBox="0 0 16 16" aria-hidden="true"><path d="M3 1l3 3-1.5 2a8 8 0 0 0 5.5 5.5L12 10l3 3-2 2C7 15 1 9 1 3z"/></svg>
        818-555-0142
      </li>
      <li>
        <svg viewBox="0 0 16 16" aria-hidden="true"><rect x="4" y="1" width="8" height="14" rx="1.5"/><rect x="5.5" y="3" width="5" height="6" fill="#156b38"/></svg>
        310-555-0187
      </li>
      <li>
        <svg viewBox="0 0 16 16" aria-hidden="true"><rect x="1" y="4" width="14" height="9"/><path d="M1 4l7 5 7-5" fill="none" stroke="#156b38" stroke-width="1.2"/></svg>
        dmorrow@lodestonerest.com
      </li>
      <li>
        <svg viewBox="0 0 16 16" aria-hidden="true"><circle cx="8" cy="8" r="6.5" fill="none" stroke="#fff" stroke-width="1.4"/><path d="M1.5 8h13M8 1.5c-3 3.5-3 9.5 0 13M8 1.5c3 3.5 3 9.5 0 13" fill="none" stroke="#fff" stroke-width="1.2"/></svg>
        lodestonerest.com
      </li>
    </ul>
  </section>

</div>
</body>
</html>
```